Leave-behind marketing postcard showing retirement plan limits for the last three years.

We need a 5x7 postcard for our company, Meridel Halvorsen, Inc. We are a third party retirement plan administration firm. The piece should include our logo, address, phone, website, and the contribution limits for the last three years - 2015, 2014, 2013 (see attached for company logo, color palette and retirement plan limits chart). You can also incorporate our slogan on one of the sides - "Providing and protecting retirement since 1983." This postcard is a leave-behind. We will not be mailing it so you don't have to include space for a stamp and address. The postcard can be 4 color on both sides. Include a bleed.

Target Market(s)

Financial advisors and business owners

Industry/Entity Type

Marketing

Font styles to use
Other font styles liked:
• Georgia and arial

Requirements
Must have
• Please use some of the colors in the attached color palette.

```html
<!DOCTYPE html>
<html lang="en">
<head>
<meta charset="utf-8">
<title>Meridel Halvorsen, Inc. – Postcard</title>
<link rel="stylesheet" href="https://fonts.googleapis.com/css2?family=Arimo:wght@400;700&family=Gelasio:wght@400;500&display=swap">
<style>
  :root{
    --backdrop:#000;
    --paper:#fff;
    --navy:#00507d;
    --band-blue:#0a5784;
    --teal:#6eacb3;
    --taupe:#b2a6a0;
    --mist:#cfd3d8;
    --ink:#111;
    --ink-navy:#0d1a44;
    --rule:#1e1e1e;
  }
  *{box-sizing:border-box;margin:0;padding:0}
  html,body{width:880px;height:1200px;overflow:hidden;background:var(--backdrop)}
  body{position:relative;font-family:"Arimo",Arial,sans-serif;color:var(--ink)}

  .card{position:absolute;left:72px;width:734px;height:538px;background:var(--paper);overflow:hidden}
  .card--front{top:39px}
  .card--back{top:619px;left:73px}

  /* front */
  .hero{position:absolute;left:39px;top:24px;width:658px;height:81px;
    background:linear-gradient(180deg,#4a6f9c 0%,#8fa7c3 45%,#c9d3de 60%,#5d7a99 80%,#2e4a6b 100%)}
  .hero__name{position:absolute;left:14px;top:24px;font:700 26px/32px "Arimo",Arial,sans-serif;color:#fff}
  .slogan{position:absolute;left:39px;top:120px;font:400 17px "Gelasio",Georgia,serif;color:#1f3f72;letter-spacing:.3px}

  .limits{position:absolute;left:39px;top:153px;width:658px;border-collapse:collapse;color:#fff;font-size:16px}
  .limits th,.limits td{border:1px solid var(--rule);padding:0}
  .limits th{background:var(--taupe);height:29px;font-weight:700;font-size:16px}
  .limits td{height:26px;text-align:center}
  .limits td:first-child{text-align:left;padding-left:22px}
  .limits tr:nth-child(odd) td{background:var(--navy)}
  .limits tr:nth-child(even) td{background:var(--teal)}
  .limits tr.tall td{height:36px;line-height:15px}
  .col-type{width:290px}.col-y1{width:131px}.col-y2{width:122px}

  .notes{position:absolute;left:39px;top:419px;font-size:11.5px;line-height:14.5px}
  .notes sup{font-size:7px}

  .contact-band{position:absolute;left:0;bottom:0;width:734px;height:71px}
  .contact-band svg{position:absolute;inset:0}
  .contact-band__info{position:absolute;left:37px;top:15px;color:#fff;font-size:15.5px;line-height:20px}
  .contact-band__info span{margin-left:14px}
  .contact-band__web{position:absolute;right:50px;top:21px;color:#fff;font-weight:700;font-size:18.5px}

  /* back */
  .header{position:absolute;left:0;top:0;width:734px;height:135px}
  .header svg{position:absolute;inset:0}
  .brand{position:absolute;left:40px;top:44px;font:700 22px/26px "Arimo",Arial,sans-serif;color:var(--ink-navy)}
  .headline{position:absolute;left:283px;top:44px;width:390px;text-align:center;color:#fff;
    font:400 31px/34px "Gelasio",Georgia,serif}

  .intro{position:absolute;left:49px;top:155px;width:635px;font-size:14.4px;line-height:17.9px;text-align:justify}
  .list-title{position:absolute;top:264px;font-weight:700;font-size:16.5px;color:var(--navy);letter-spacing:.6px}
  .list{position:absolute;top:288px;list-style:none;font-size:15.5px}
  .list li{height:24.3px;line-height:24px}
  .plans{left:49px}
  .clients{left:341px}
  .clients li.double{height:45px;line-height:16px;padding-top:8px}
  .site{position:absolute;left:49px;top:484px;font-weight:700;font-size:21px;color:var(--navy)}
  .cta{position:absolute;right:47px;top:455px;text-align:right;color:var(--ink)}
  .cta__lead{font-weight:700;font-size:18.5px;letter-spacing:.3px}
  .cta__phone{font-weight:700;font-size:30.5px;margin-top:2px}
</style>
</head>
<body>

<section class="card card--front">
  <div class="hero" role="img" aria-label="Photograph of a wooden pier and gazebo over calm water at dusk">
    <div class="hero__name">Meridel Halvorsen, Inc.</div>
  </div>
  <h2 class="slogan">PROVIDING AND PROTECTING RETIREMENT SINCE 1983</h2>

  <table class="limits">
    <colgroup><col class="col-type"><col class="col-y1"><col class="col-y2"><col></colgroup>
    <thead><tr><th>Type of Limitation</th><th>2015</th><th>2014</th><th>2013</th></tr></thead>
    <tbody>
      <tr><td>401(k) / 403 (b) Elective Deferrals</td><td>$18,000</td><td>$17,500</td><td>$17,500</td></tr>
      <tr><td>Catch-up amount</td><td>$6,000</td><td>$5,500</td><td>$5,500</td></tr>
      <tr><td>Defined Benefit Plans</td><td>$210,000</td><td>$210,000</td><td>$205,000</td></tr>
      <tr><td>Defined Contribution Plan</td><td>$53,000</td><td>$52,000</td><td>$51,000</td></tr>
      <tr><td>Annual Compensation Limit</td><td>$265,000</td><td>$260,000</td><td>$255,000</td></tr>
      <tr><td>Highly Compensated Employees</td><td>$120,000</td><td>$115,000</td><td>$115,000</td></tr>
      <tr><td>Key employee officer threshold</td><td>$170,000</td><td>$170,000</td><td>$165,000</td></tr>
      <tr class="tall"><td>Income Subject to Social<br>Security Tax</td><td>$118,500</td><td>$117,000</td><td>$113,700</td></tr>
    </tbody>
  </table>

  <div class="notes">
    <p>*For individuals age 50 and older</p>
    <p><sup>1</sup>Based on plan year ending in calendar year</p>
    <p><sup>2</sup>Based on plan year beginning in calendar year</p>
  </div>

  <footer class="contact-band">
    <svg width="734" height="71" viewBox="0 0 734 71" aria-hidden="true">
      <rect width="734" height="71" fill="var(--taupe)"/>
      <polygon points="0,0 417,0 486,71 0,71" fill="var(--band-blue)"/>
    </svg>
    <div class="contact-band__info">
      <p>1480 Harbor View Ave., Suite 210, Marlow CA 90412</p>
      <p>Phone: 310-555-0184<span>Fax: 310-555-0185</span></p>
    </div>
    <div class="contact-band__web">www.mhibenefits.com</div>
  </footer>
</section>

<section class="card card--back">
  <header class="header">
    <svg width="734" height="135" viewBox="0 0 734 135" aria-hidden="true">
      <rect width="734" height="135" fill="var(--navy)"/>
      <polygon points="0,0 194,0 263,135 0,135" fill="var(--mist)"/>
    </svg>
    <div class="brand">Meridel<br>Halvorsen, Inc.</div>
    <h1 class="headline">Providing And Protecting Retirement Since 1983</h1>
  </header>

  <p class="intro">We are a highly experienced Third Party Administration firm that handles all aspects of your company’s retirement plan, except the investments. As consultants, we help to strategically design your plan, saving you time and money. The increasingly complex retirement plan industry is full of critical dates and deadlines. Our expert staff and cutting-edge technology ensure that we deliver on the expectations for every plan we design and administer.</p>

  <h3 class="list-title plans">PLAN TYPES</h3>
  <ul class="list plans">
    <li>401(k) Plans</li>
    <li>403(b) and 457(b) Plans</li>
    <li>Profit Sharing Plans</li>
    <li>Traditional Defined Benefit Plans</li>
    <li>Cash Balance Plans</li>
    <li>Money Purchase Pension Plans</li>
    <li>Combination Plans</li>
  </ul>

  <h3 class="list-title clients">CLIENT TYPES</h3>
  <ul class="list clients">
    <li>Entrepreneurial</li>
    <li>Professional</li>
    <li class="double">Professionally managed entities<br>(including Private Equity)</li>
    <li>Publicly Traded</li>
  </ul>

  <p class="site">www.mhibenefits.com</p>
  <div class="cta">
    <p class="cta__lead">SCHEDULE A FREE CONSULTATION</p>
    <p class="cta__phone">CALL US: 310-555-0184</p>
  </div>
</section>

</body>
</html>
```